Website design for commercial and residential security company

we're looking to see some new designs for an established company with no website.

homepage and one inner page

here is a link to the homepage content, sitemap, logo and more.
https://files.trovelink-share.net/folders/7QmzKpw3RtvxnLa9eHs2YcdJfuoPb?view=open

call to action should be Request A Quote

if you have any questions please send them to us asap

thank you

Number of Pages Required

1 page

Font styles to use
Sans Serif

```html
<!DOCTYPE html>
<html lang="en">
<head>
<meta charset="utf-8">
<title>Beacon Ridge Security</title>
<link href="https://fonts.googleapis.com/css2?family=Poppins:wght@400;500;600;700&family=Lato:wght@400;700&display=swap" rel="stylesheet">
<style>
:root{
  --gold:#c9a22d;
  --gold-dark:#b18d22;
  --ink:#1e1e1e;
  --text:#2b2b2b;
  --grey:#9a9a9a;
  --dark:#1b1b1b;
  --white:#ffffff;
}
*{margin:0;padding:0;box-sizing:border-box}
html,body{width:1200px;height:3849px;overflow:hidden}
body{position:relative;background:var(--white);font-family:'Lato',sans-serif;color:var(--text)}
.abs{position:absolute}
.head{font-family:'Poppins',sans-serif}
.btn{position:absolute;display:flex;align-items:center;justify-content:center;gap:8px;font-family:'Poppins',sans-serif;font-weight:600;font-size:15px;color:var(--white);background:var(--gold);border-radius:2px;letter-spacing:.2px}
.btn svg{width:14px;height:14px}

/* hero */
.hero-photo{left:0;top:0;width:1200px;height:811px;background:linear-gradient(160deg,#3f5160 0%,#5b7080 35%,#6e7c86 60%,#2c3740 100%)}
.camera{left:720px;top:0;width:330px;height:610px;border-radius:0 0 165px 165px;background:radial-gradient(circle at 50% 65%,#f2f2f2 0%,#cfd2d4 45%,#8f969b 100%)}
.logo{left:64px;top:46px;display:flex;align-items:center;gap:10px;font-family:'Poppins',sans-serif;font-weight:600;font-size:26px;color:var(--white)}
.logo i{width:34px;height:34px;border-radius:50%;background:var(--gold);display:block}
.nav{left:428px;top:62px;display:flex;gap:32px;font-family:'Poppins',sans-serif;font-weight:500;font-size:17.5px;color:var(--white)}
.nav-quote{left:944px;top:53px;width:180px;height:45px;font-size:14px}
.hero-ring{left:102px;top:187px;width:448px;height:448px;border-radius:50%;background:#a7a7a7}
.hero-disc{left:126px;top:211px;width:400px;height:400px;border-radius:50%;background:var(--gold);text-align:center;color:var(--white)}
.hero-disc .t1{margin-top:56px;font-family:'Poppins',sans-serif;font-weight:700;font-size:40px;line-height:46px}
.hero-disc .t2{font-family:'Poppins',sans-serif;font-size:34px;line-height:40px}
.hero-disc .t3{margin-top:8px;font-family:'Poppins',sans-serif;font-weight:700;font-size:37px;line-height:42px}
.hero-cta{left:215px;top:511px;width:218px;height:53px;background:var(--white);color:var(--ink)}
.dots{left:553px;top:686px;display:flex;gap:6px}
.dots span{width:15px;height:15px;border-radius:50%;border:2px solid var(--white)}
.dots span.on{background:var(--white)}

/* mission */
.h2{font-family:'Poppins',sans-serif;font-weight:600;font-size:40px;color:var(--ink);line-height:1.2}
.mission-title{left:143px;top:886px}
.rule{height:3px;background:var(--gold)}
.mission-lead{left:144px;top:984px;width:430px;font-size:16px;font-weight:700;line-height:25.5px}
.mission-body{left:144px;top:1074px;width:430px;font-size:16px;line-height:24px}
.mission-ring{left:610px;top:846px;width:448px;height:448px;border-radius:50%;background:conic-gradient(#9a9a9a 0 60%,#7a7a7a 60% 100%)}
.mission-photo{left:634px;top:870px;width:400px;height:400px;border-radius:50%;background:linear-gradient(135deg,#f1f1ef 0%,#dcdcd8 55%,#b98a5a 100%);border:8px solid var(--white)}

/* commercial */
.commercial{left:0;top:1367px;width:1200px;height:819px;background:radial-gradient(ellipse at 50% 40%,#3a3a3a 0%,#1d1d1d 60%,#0f0f0f 100%)}
.com-title{left:0;top:1420px;width:1200px;text-align:center;color:var(--white)}
.com-sub{left:0;top:1537px;width:1200px;text-align:center;font-family:'Poppins',sans-serif;font-size:18px;color:var(--white)}
.com-text{left:140px;top:1574px;width:920px;text-align:center;font-family:'Poppins',sans-serif;font-size:16px;line-height:26px;color:var(--white)}
.card{position:absolute;border:2px solid #e6e6e6;display:flex;align-items:center;gap:20px;padding:0 18px;color:var(--white);font-family:'Poppins',sans-serif;font-size:18.5px;line-height:24px}
.card svg{flex:none;fill:none;stroke:var(--gold);stroke-width:3}

/* residential */
.res-main{left:143px;top:2276px;width:468px;height:314px;background:linear-gradient(160deg,#d8cdbb 0%,#c7a47d 45%,#5e6f85 100%)}
.res-a{left:157px;top:2596px;width:212px;height:210px;background:linear-gradient(150deg,#e8e3da,#8f8a82)}
.res-b{left:387px;top:2596px;width:212px;height:210px;background:linear-gradient(150deg,#d8dfe3,#b33c34 70%,#2f2f2f)}
.res-frame{left:148px;top:2587px;width:460px;height:228px;background:#e9e9e9}
.res-title{left:660px;top:2270px}
.res-lead{left:662px;top:2408px;width:410px;font-size:19px;font-weight:700;line-height:27px}
.res-body{left:662px;top:2502px;width:400px;font-size:16px;line-height:25.5px}

/* quote */
.quote-bg{left:0;top:2891px;width:1200px;height:569px}
.q-title{left:0;top:3020px;width:1200px;text-align:center;color:var(--white)}
.field{position:absolute;background:var(--white);border:1px solid #e2e2e2;font-size:14px;color:#444;padding:14px 21px}
.submit{left:509px;top:3330px;width:181px;height:45px;background:#141414;border-radius:2px}

/* footer */
.footer{left:0;top:3460px;width:1200px;height:389px;background:var(--dark)}
.f-ico{position:absolute;width:46px;height:46px;border-radius:50%;background:var(--white);display:flex;align-items:center;justify-content:center}
.f-ico svg{width:20px;height:20px;fill:var(--gold)}
.f-txt{position:absolute;left:210px;font-size:16px;line-height:24px;color:var(--white)}
.f-email{left:584px;top:3523px;width:313px;height:39px;border-radius:20px;background:var(--white);font-size:13px;color:#555;padding:11px 22px}
.f-sub{left:913px;top:3523px;width:142px;height:39px;border-radius:20px;font-size:14px}
.f-nav{right:145px;top:3591px;display:flex;gap:14px;font-size:16px;font-weight:700;color:var(--white)}
.f-social{display:flex;gap:11px;left:920px;top:3641px}
.f-social span{width:38px;height:38px;border-radius:50%;border:2px solid #cfcfcf}
.f-line{left:542px;top:3480px;width:1px;height:260px;background:#2c2c2c}
.copy{left:0;top:3786px;width:1200px;text-align:center;font-size:16px;font-weight:700;color:var(--white)}
</style>
</head>
<body>

<!-- hero -->
<div class="abs hero-photo" role="img" aria-label="Modern office interior with a dome security camera"></div>
<div class="abs camera" role="img" aria-label="Ceiling mounted dome security camera"></div>
<svg class="abs" style="left:0;top:680px" width="1200" height="140" viewBox="0 0 1200 140">
  <polygon points="0,22 418,118 1200,10 1200,140 0,140" fill="#fff"/>
  <polygon points="0,22 418,112 1200,0 1200,14 418,131 0,40" fill="#c9a22d"/>
  <polygon points="0,40 418,131 1200,14 1200,140 0,140" fill="#fff"/>
</svg>
<div class="abs logo"><i></i>Beacon Ridge Security</div>
<nav class="abs nav"><span>Home</span><span>About</span><span>Solutions</span><span>Resources</span><span>Contact</span></nav>
<div class="btn nav-quote">REQUEST A QUOTE</div>
<div class="abs hero-ring"></div>
<div class="abs hero-disc">
  <div class="t1">Beacon Ridge</div>
  <div class="t2">Security</div>
  <div class="t3">Residential<br>And Commercial<br>Property</div>
</div>
<div class="btn hero-cta">REQUEST A QUOTE <svg viewBox="0 0 14 14"><path d="M1 7h11M8 3l4 4-4 4" stroke="#1e1e1e" stroke-width="2.2" fill="none"/></svg></div>
<div class="abs dots"><span></span><span></span><span class="on"></span><span></span><span></span></div>

<!-- mission -->
<h2 class="abs h2 mission-title">Our Mission</h2>
<div class="abs rule" style="left:143px;top:959px;width:97px"></div>
<p class="abs mission-lead">To provide our customers with comprehensive security, audio/video, and automation with top notch customer service. We Ensure Security with Smart Tools.</p>
<p class="abs mission-body">The graded security measures from Beacon Ridge Security ensure the safety of both residential and commercial property. We provide a wide range of Residential and Commercial Security Solutions.</p>
<div class="btn" style="left:144px;top:1201px;width:176px;height:49px">LEARN MORE <svg viewBox="0 0 14 14"><path d="M1 7h11M8 3l4 4-4 4" stroke="#fff" stroke-width="2.2" fill="none"/></svg></div>
<div class="abs mission-ring"></div>
<div class="abs mission-photo" role="img" aria-label="Hand pressing keys on a wall mounted alarm keypad"></div>

<!-- commercial -->
<div class="abs commercial" role="img" aria-label="Dim commercial interior with ceiling speakers"></div>
<h2 class="abs h2 com-title">Commercial Solutions</h2>
<div class="abs" style="left:549px;top:1500px;width:102px;height:3px;background:#fff"></div>
<p class="abs com-sub">Protect assets and security of your business with Exceptional Commercial Security Installation</p>
<p class="abs com-text">People's safety is our top priority. This includes ensuring that the security system built at your commercial property is configured accurately. Further, it will protect against intruders, burglaries, and holdups. We do this by:</p>

<div class="card" style="left:143px;top:1659px;width:290px;height:171px">
  <svg width="110" height="110" viewBox="0 0 110 110"><rect x="30" y="14" width="60" height="44" rx="4"/><rect x="14" y="34" width="62" height="48" rx="4"/><path d="M38 48v22l18-11z"/><path d="M20 90h50"/></svg>
  <span>Audio &amp; Video Solutions for your commercial property</span>
</div>
<div class="card" style="left:445px;top:1659px;width:245px;height:171px">
  <svg width="100" height="110" viewBox="0 0 100 110"><rect x="8" y="40" width="58" height="40" rx="4"/><path d="M20 40V18"/><rect x="18" y="52" width="18" height="12"/><path d="M58 64l20-8 18 8v16c0 14-10 22-18 24-8-2-20-10-20-24z"/></svg>
  <span>Burglar Alarms &amp; Detectors</span>
</div>
<div class="card" style="left:701px;top:1659px;width:355px;height:171px">
  <svg width="110" height="110" viewBox="0 0 110 110"><rect x="16" y="30" width="78" height="50" rx="3"/><path d="M6 84h98"/><path d="M44 70V50a11 11 0 0 1 22 0v20zM40 70h30"/><path d="M34 40l-6-4M76 40l6-4M55 28v-6"/></svg>
  <span>Alarm systems and cameras precisely installed so that more of your property is tracked.</span>
</div>
<div class="card" style="left:143px;top:1839px;width:456px;height:193px">
  <svg width="110" height="110" viewBox="0 0 110 110"><path d="M14 20l50 14-6 16-50-14z"/><path d="M18 40v40M10 60h10"/><circle cx="74" cy="74" r="26"/><path d="M62 72a17 17 0 0 1 24 0M67 78a9 9 0 0 1 14 0"/><circle cx="74" cy="86" r="2"/></svg>
  <span>CCTV cameras equipped with facial recognition technologies enable the technology to identify the offenders.</span>
</div>
<div class="card" style="left:611px;top:1839px;width:445px;height:193px">
  <svg width="120" height="110" viewBox="0 0 120 110"><rect x="8" y="22" width="64" height="76" rx="3"/><circle cx="40" cy="50" r="16"/><circle cx="40" cy="50" r="6"/><rect x="72" y="40" width="38" height="50"/><path d="M16 80h48M80 54h20M80 66h20M80 78h20"/></svg>
  <span>Monitoring of alarms and video recordings 24 hours a day, seven days a week. Addressing all the incidents with an urgent response.</span>
</div>
<div class="btn" style="left:512px;top:2074px;width:177px;height:47px">LEARN MORE <svg viewBox="0 0 14 14"><path d="M1 7h11M8 3l4 4-4 4" stroke="#fff" stroke-width="2.2" fill="none"/></svg></div>

<!-- residential -->
<div class="abs res-main" role="img" aria-label="Family sitting at home under a cardboard roof"></div>
<div class="abs res-frame"></div>
<div class="abs res-a" role="img" aria-label="Phone showing a live home camera view"></div>
<div class="abs res-b" role="img" aria-label="Technician testing a ceiling detector with a multimeter"></div>
<h2 class="abs h2 res-title">Residential<br>Security Solutions</h2>
<div class="abs" style="left:662px;top:2380px;width:101px;height:3px;background:#a6a6a6"></div>
<p class="abs res-lead">Consider a home surveillance device that would do more for you and your family than you ever imagined.</p>
<p class="abs res-body">Beacon Ridge Security is your trustable security provider. Also, as certified professionals carry out the installation, you have everything under control. Your home is being securely watched from various points, with cameras capable of tracking any intruder's path. Specifically, we offer Residential Intrusion Detection Security Systems, Residential Alarm, Residential Network Wi-Fi, CCTVs and residential home automation.</p>
<div class="btn" style="left:662px;top:2752px;width:313px;height:49px">GET IN TOUCH WITH US TODAY <svg viewBox="0 0 14 14"><path d="M1 7h11M8 3l4 4-4 4" stroke="#fff" stroke-width="2.2" fill="none"/></svg></div>

<!-- quote -->
<svg class="abs quote-bg" viewBox="0 0 1200 569" role="img" aria-label="Gold toned backdrop of a security control panel">
  <defs><linearGradient id="qg" x1="0" y1="0" x2="1" y2="1"><stop offset="0" stop-color="#c9a22d"/><stop offset=".6" stop-color="#c6a03a"/><stop offset="1" stop-color="#b8922a"/></linearGradient></defs>
  <polygon points="0,104 829,0 1200,109 1200,569 0,569" fill="url(#qg)"/>
  <polygon points="800,4 829,0 1200,109 1200,116" fill="#a7a7a7"/>
</svg>
<h2 class="abs h2 q-title">Request A Quote</h2>
<div class="abs" style="left:563px;top:3090px;width:74px;height:3px;background:#fff"></div>
<div class="field" style="left:194px;top:3124px;width:396px;height:48px">First Name</div>
<div class="field" style="left:610px;top:3124px;width:396px;height:48px">Last Name</div>
<div class="field" style="left:194px;top:3188px;width:396px;height:48px">Email Address</div>
<div class="field" style="left:610px;top:3188px;width:396px;height:112px">Message</div>
<div class="field" style="left:194px;top:3252px;width:396px;height:48px">Phone Number</div>
<div class="btn submit">SUBMIT</div>

<!-- footer -->
<div class="abs footer"></div>
<div class="abs f-line"></div>
<div class="f-ico" style="left:143px;top:3508px"><svg viewBox="0 0 20 20"><path d="M10 1a6.5 6.5 0 0 0-6.5 6.5C3.5 12 10 19 10 19s6.5-7 6.5-11.5A6.5 6.5 0 0 0 10 1zm0 9a2.5 2.5 0 1 1 0-5 2.5 2.5 0 0 1 0 5z"/></svg></div>
<div class="f-txt" style="top:3507px">100 enim ipsam voluptatem<br>quia voluptas sit</div>
<div class="f-ico" style="left:143px;top:3577px"><svg viewBox="0 0 20 20"><path d="M5 2l3 4-2 2c1 2 3 4 5 5l2-2 4 3-2 3C9 17 3 11 2 5z"/></svg></div>
<div class="f-txt" style="top:3576px">Phone :<br>555-0142 7789</div>
<div class="f-ico" style="left:143px;top:3645px"><svg viewBox="0 0 20 20"><path d="M2 5h16v10H2z"/><path d="M2 5l8 6 8-6" stroke="#fff" stroke-width="1.5" fill="none"/></svg></div>
<div class="f-txt" style="top:3645px">Email :<br>info@beaconridgesecurity.com</div>
<div class="abs f-email">Enter email</div>
<div class="btn f-sub">SUBSCRIBE</div>
<nav class="abs f-nav"><span>Home</span><span>|</span><span>About</span><span>|</span><span>Solutions</span><span>|</span><span>Resources</span><span>|</span><span>Contact</span></nav>
<div class="abs f-social"><span></span><span></span><span></span></div>
<p class="abs copy">Beacon Ridge Security © 2021 All Rights Reserved | term and condition</p>

</body>
</html>
```